Küchenparty
Zielgruppe
Restaurant / Catering / Event Management
Zielgruppe ü 40
Aufgabenstellung
Klares, schlichtes und vorallem edles design
Den Valentinstag mal anders feiern?
mischen Sie sich mit Ihren Liebsten ins getrubel einer Großküche und erleben das exclusive Küchenflair!
Bunte Diskobeläuchtung, Musik und Gäste in der Küche....das gibt es nur zu ganz besonderen Anlässen!
Endlich haben Sie in unserer komplett neu renovierten Küche wieder die Möglichkeit unseren Köchen und Köchinnen über die Schulter zu schauen oder über Rezepte fachzusimpeln.
Wir freuen uns Sie zur ersten Küchenparty im Lindmarks am See begrüßen zu dürfen!
Es erwartet Sie eine Veilzahl an speziell für Sie angerichteten Speisen.
Dazu genießen Sie Weine regionaler Weingüter und aus Italien.
Speisen und Getränke inclusive!
Preis pro Person 98€
Den Valentinstag mal anders beginnen;
mit höchstem Genuss aus Küche und Keller bei der Küchenparty im Lindmks am See.
Schlagsworte:
Für Sie individuell angerichtete Speisen / die Küche in action für Sie!
Weine der Region
DJ und Party
Preis 98,00 €
inklusive:
Aperitif
Große Speisenvarietät (5 Gänge plus)
Regionale und italienische Weine
Logo muss vorhanden sein in rot odeer weiss
Kontaktdaten:
Lindmarks am See
Lore-Falk platz 7
71058 Seewalden
Tel: 07199 38 716 0
Mail: event@lindmarks.de
www.lindmarks.de

```html
<!DOCTYPE html>
<html lang="de">
<head>
<meta charset="utf-8">
<title>Küchenparty – Lindmarks am See</title>
<link rel="stylesheet" href="https://fonts.googleapis.com/css2?family=Raleway:wght@200;300&family=Roboto+Condensed:wght@300;400;700&display=swap">
<style>
  :root {
    --tan: #dcbc94;
    --white: #ffffff;
    --paper: #ffffff;
    --stage: #f1efec;
    --band-grey: #6f6d6b;
    --food-light: #f4f2f0;
    --food-warm: #e7c07c;
    --room-dark: #2a1c12;
    --room-warm: #c98e4c;
  }
  * { box-sizing: border-box; margin: 0; padding: 0; }
  html, body {
    width: 848px; height: 1200px; overflow: hidden;
    background: var(--stage);
  }
  .flyer {
    position: absolute; left: 139px; top: 20px;
    width: 570px; height: 1160px;
    background: var(--paper);
    box-shadow: 0 4px 18px rgba(0,0,0,.12);
    font-family: "Roboto Condensed", "Arial Narrow", sans-serif;
    font-weight: 300;
    color: var(--white);
  }
  .hero-food {
    position: absolute; left: 15px; top: 15px; width: 540px; height: 375px;
    background: radial-gradient(ellipse at 72% 52%, var(--food-warm) 0%, #efd7ab 28%, var(--food-light) 62%);
  }
  .price-badge {
    position: absolute; left: 0; top: 0; width: 228px; height: 228px;
    border-radius: 50%;
    background: var(--tan);
    border: 5px solid var(--white);
    display: flex; flex-direction: column; justify-content: center; align-items: center;
    text-align: center; font-size: 18px; line-height: 1.3;
  }
  .title-band {
    position: absolute; left: 15px; top: 396px; width: 540px; height: 210px;
    background: var(--tan);
    text-align: center;
  }
  .title {
    font-family: "Raleway", "Helvetica Neue", sans-serif;
    font-weight: 200; font-size: 66px; letter-spacing: 1px;
    margin-top: 36px; line-height: 1;
  }
  .intro {
    margin-top: 26px; font-size: 18px; line-height: 1.38;
  }
  .hero-room {
    position: absolute; left: 15px; top: 612px; width: 540px; height: 218px;
    background: linear-gradient(90deg, var(--room-dark) 0%, #5a3b22 40%, var(--room-warm) 75%, #f3d9a6 100%);
  }
  .tag-band {
    position: absolute; left: 0; top: 830px; width: 570px; height: 46px;
    background: var(--band-grey);
    display: flex; align-items: center; justify-content: center;
    font-size: 17px; white-space: nowrap;
  }
  .footer {
    position: absolute; left: 15px; top: 896px; width: 540px; height: 232px;
    background: var(--tan);
    text-align: center;
  }
  .wordmark {
    margin-top: 56px; font-size: 40px; font-weight: 400; letter-spacing: 1px;
  }
  .contact {
    margin-top: 30px; font-size: 17px; line-height: 1.4;
  }
  .web { font-weight: 700; }
</style>
</head>
<body>
  <main class="flyer">
    <div class="hero-food" role="img" aria-label="Foto: frische Bandnudeln mit Basilikum auf hellem Grund"></div>
    <div class="price-badge">
      <span>Preis 98,00 €</span>
      <span>inkl. Apéritif</span>
      <span>Große Speisenvarietät</span>
      <span>(5 Gänge plus)</span>
      <span>Regionale und</span>
      <span>italienische Weine</span>
    </div>

    <section class="title-band">
      <h1 class="title">KÜCHENPARTY</h1>
      <p class="intro">Den Valentinstag mal anders beginnen:<br>
        mit höchstem Genuss aus Küche und Keller<br>
        bei der Küchenparty im Lindmks am See.</p>
    </section>

    <div class="hero-room" role="img" aria-label="Foto: festlich gedeckter Restaurantsaal mit warmer Beleuchtung"></div>

    <div class="tag-band">Weine der Region | DJ und Party | Für Sie individuell angerichtete Speisen</div>

    <footer class="footer">
      <div class="wordmark">Lindmarks am See</div>
      <p class="contact">
        Lindmarks am See | Lore-Falk platz 7 | 71058 Seewalden<br>
        Tel: 07199 38 716 0 | Mail: event@lindmarks.de<br>
        <span class="web">www.lindmarks.de</span>
      </p>
    </footer>
  </main>
</body>
</html>
```